Business card design needed

We are a gardening company who handle:
All Forms of gardens work including
Mowing
Pruning
edging
weeding
Poisoning
Landscaping
Minor Stump Removal
Rubbish Removal
and more

I want a card that look professional not cartoon style

Industry/Entity Type

Business

Contact Information for Business Card

Fernhollow Yard and Lawn Service

Greg Halden
0486152938

```html
<!DOCTYPE html>
<html lang="en">
<head>
<meta charset="utf-8">
<title>Fernhollow Yard and Lawn Service – Business Card</title>
<link rel="stylesheet" href="https://fonts.googleapis.com/css2?family=Mulish:ital,wght@0,400;0,500;0,700;1,400&display=swap">
<style>
  :root {
    --card-bg: #ffffff;
    --lime: #a8e321;
    --lime-light: #c4ef4a;
    --ink: #222222;
    --ink-soft: #3a3a3a;
    --leaf: #3f7d3a;
    --grass-dark: #3f8f2a;
    --grass-light: #9fd65a;
    --mower-dark: #2b2b2b;
  }
  * { margin: 0; padding: 0; box-sizing: border-box; }
  html, body {
    width: 1200px; height: 698px; overflow: hidden;
    background: var(--card-bg);
  }
  .card {
    position: relative;
    width: 1200px; height: 698px;
    background: var(--card-bg);
    font-family: "Mulish", sans-serif;
    color: var(--ink);
    overflow: hidden;
  }
  .mower-illustration {
    position: absolute;
    left: 8px; top: 34px;
    width: 340px; height: 205px;
    border-radius: 30px 60px 20px 20px;
    background: linear-gradient(135deg, var(--mower-dark) 0%, var(--mower-dark) 40%, var(--lime) 60%, var(--lime-light) 100%);
  }
  .contact {
    position: absolute;
    right: 50px; top: 64px;
    display: flex; align-items: center; gap: 10px;
    font-size: 35px; color: var(--ink-soft);
  }
  .contact .phone-number { font-weight: 700; color: var(--ink); }
  .contact svg { width: 28px; height: 28px; }
  .name-band {
    position: absolute;
    left: 0; top: 136px;
    width: 1200px; height: 91px;
  }
  .name-band svg { position: absolute; inset: 0; }
  .company-name {
    position: absolute;
    left: 350px; top: 0; height: 91px;
    display: flex; align-items: center;
    font-size: 42px; font-weight: 700; color: var(--ink);
  }
  .intro {
    position: absolute; left: 0; right: 0; top: 268px;
    text-align: center;
    font-size: 35px; font-weight: 700; color: var(--ink);
  }
  .services {
    position: absolute; left: 0; right: 0; top: 340px;
    text-align: center;
    font-size: 33px; line-height: 43px; color: var(--ink-soft);
  }
  .services .dot { margin: 0 14px; font-size: 22px; vertical-align: middle; }
  .offer {
    position: absolute; left: 0; right: 0; top: 494px;
    text-align: center;
    font-size: 35px; font-style: italic; color: var(--leaf);
  }
  .grass-illustration {
    position: absolute;
    left: 0; top: 540px; width: 1200px; height: 145px;
    background: linear-gradient(180deg, rgba(159,214,90,0) 0%, var(--grass-light) 45%, var(--grass-dark) 100%);
  }
  .base-strip {
    position: absolute; left: 0; bottom: 0;
    width: 1200px; height: 13px;
    background: var(--lime);
  }
</style>
</head>
<body>
<main class="card">
  <div class="mower-illustration" role="img" aria-label="Illustration of a lime green and black lawn mower"></div>

  <p class="contact">
    <span class="person-name">Greg Halden</span>
    <svg viewBox="0 0 24 24" aria-hidden="true"><path fill="#333" d="M6.6 10.8a15.1 15.1 0 0 0 6.6 6.6l2.2-2.2a1 1 0 0 1 1-.25 11.4 11.4 0 0 0 3.6.57 1 1 0 0 1 1 1V20a1 1 0 0 1-1 1A17 17 0 0 1 3 4a1 1 0 0 1 1-1h3.5a1 1 0 0 1 1 1c0 1.25.2 2.45.57 3.57a1 1 0 0 1-.25 1z"/></svg>
    <span class="phone-number">0486152938</span>
  </p>

  <div class="name-band">
    <svg width="1200" height="91" viewBox="0 0 1200 91" aria-hidden="true">
      <polygon points="330,0 1200,0 1200,91 305,91" fill="var(--lime)"/>
    </svg>
    <h1 class="company-name">Fernhollow Yard and Lawn Service</h1>
  </div>

  <p class="intro">All Forms of gardens work including</p>

  <p class="services">
    Mowing<span class="dot">●</span>Pruning<span class="dot">●</span>Edging<span class="dot">●</span>Weeding<span class="dot">●</span>Poisoning<br>
    Landscaping<span class="dot">●</span>Minor Stump Removal<span class="dot">●</span>Rubbish Removal<br>
    and more
  </p>

  <p class="offer">Free Quotes and Discounts for Pensioners</p>

  <div class="grass-illustration" role="img" aria-label="Illustration of a row of green grass blades"></div>
  <div class="base-strip"></div>
</main>
</body>
</html>
```